Brennoria Business Card Design

Primarily a Real Estate Investment company but also invests in other business ventures.
Updates

The attachments have been uploaded to give you a better perspective on what I'm looking for. Please pay close attention to the Tidal Gala Works card as a sample.Thank you.

Target Market(s)

Upper escalante individuals that would like to purchase real estate

Industry/Entity Type

Business

Contact Information for Business Card

Brennoria Holdings LLC, Sorelle A. Vantwick, CEO/MBA, 415-286-7304, Sorelle4816@mailbrook.net

Colors
0455a3
ffffff

Requirements
Must have
• Majority of card color MUST be Black ----- Like pictures 2&3
(pic4) Raised silver foil "B" to start the Brennoria name on the card.
(pic3) Love the whole layout, round edges, placement of contact info. {It is clean and elegant}
(pic1) Matte & Gloss backing
(pic2) Blue color (maybe the remainder of company name to make the card have pop of color).
Nice to have
• Silver foil siding

```html
<!DOCTYPE html>
<html lang="en">
<head>
<meta charset="utf-8">
<title>Brennoria Holdings LLC – Business Card</title>
<link href="https://fonts.googleapis.com/css2?family=Cinzel:wght@400;600&family=Open+Sans:wght@400;600&display=swap" rel="stylesheet">
<style>
  :root {
    --backdrop: #e9e7e4;
    --card-deep: #070d0e;
    --card-mid: #122022;
    --silver: #d9dcdd;
    --silver-dim: #9aa1a3;
    --accent-blue: #1d8fd8;
    --rule-blue: #1a86cc;
    --ink-white: #f2f4f5;
    --ink-grey: #8f9799;
  }
  * { box-sizing: border-box; margin: 0; padding: 0; }
  html, body {
    width: 1200px;
    height: 800px;
    overflow: hidden;
    background: var(--backdrop);
  }
  .canvas {
    position: relative;
    width: 1200px;
    height: 800px;
  }
  .card {
    position: absolute;
    border-radius: 6px;
    background: radial-gradient(ellipse at 60% 35%, var(--card-mid) 0%, var(--card-deep) 75%);
    box-shadow: 0 6px 18px rgba(0, 0, 0, 0.25);
    overflow: hidden;
  }

  /* Back of card – portrait */
  .card-back {
    left: 90px;
    top: 138px;
    width: 300px;
    height: 525px;
  }
  .card-back .company-vertical {
    position: absolute;
    left: 180px;
    top: 140px;
    writing-mode: vertical-rl;
    font-family: "Cinzel", serif;
    font-weight: 600;
    font-size: 20px;
    letter-spacing: 1px;
    color: var(--silver);
    text-shadow: 0 0 6px rgba(255, 255, 255, 0.25);
    white-space: nowrap;
  }

  /* Front of card – landscape */
  .card-front {
    left: 450px;
    top: 200px;
    width: 700px;
    height: 400px;
  }
  .card-front .company-name {
    position: absolute;
    right: 48px;
    top: 62px;
    font-family: "Cinzel", serif;
    font-weight: 600;
    font-size: 30px;
    letter-spacing: 1px;
    color: var(--accent-blue);
    white-space: nowrap;
  }
  .card-front .holder {
    position: absolute;
    left: 44px;
    top: 130px;
  }
  .holder .holder-name {
    font-family: "Cinzel", serif;
    font-weight: 600;
    font-size: 24px;
    color: var(--ink-white);
    letter-spacing: 0.5px;
    text-shadow: 0 0 5px rgba(255, 255, 255, 0.2);
  }
  .holder .holder-title {
    margin-top: 4px;
    font-family: "Open Sans", sans-serif;
    font-size: 12px;
    color: var(--ink-grey);
    letter-spacing: 0.5px;
  }
  .card-front .divider {
    position: absolute;
    left: 44px;
    right: 30px;
    top: 192px;
    height: 2px;
    background: var(--rule-blue);
  }
  .card-front .contact {
    position: absolute;
    left: 300px;
    top: 262px;
    font-family: "Open Sans", sans-serif;
    font-weight: 600;
    font-size: 18px;
    line-height: 1.7;
    color: var(--ink-white);
    letter-spacing: 0.5px;
    text-transform: uppercase;
    text-shadow: 0 0 6px rgba(255, 255, 255, 0.3);
  }
</style>
</head>
<body>
  <main class="canvas">
    <section class="card card-back" aria-label="Card back">
      <p class="company-vertical">Brennoria Holdings LLC</p>
    </section>

    <section class="card card-front" aria-label="Card front">
      <p class="company-name">Brennoria Holdings LLC</p>
      <div class="holder">
        <p class="holder-name">Sorelle A. Vantwick</p>
        <p class="holder-title">CEO/MBA</p>
      </div>
      <div class="divider"></div>
      <div class="contact">
        <p class="contact-phone">415-286-7304</p>
        <p class="contact-email">Sorelle4816@mailbrook.net</p>
      </div>
    </section>
  </main>
</body>
</html>
```